Banner ad for hyper local news site

We need a banner (that we will use on our own site) to explain to people that they can "be the reporter" in their local area. Lanternway is an Australia community news network. We cover local news on a daily basis but also allow people and organisations to publish their own news direct to the site. We are trying to encourage local dialogue and to empower people to talk about the things that matter to them and get their issues on the news agenda.

We need a 'call to action' banner that explains to our users that they can post their own stories on the site.

Some suggested text (thinking this would be rolling)

*Lanternway is YOUR voice in the community
*You can 'be the reporter' and write your own news
*To be heard, contribute your stories, click here - it's free

The banner doesn't have to be slick - we'd prefer a warm and friendly community feeling....but also something in keeping with the look and feel of our site wwww.lanternway-example.com.au

Industry/Entity Type

News

```html
<!DOCTYPE html>
<html lang="en">
<head>
<meta charset="utf-8">
<title>Lanternway – Be the Reporter banner storyline</title>
<link href="https://fonts.googleapis.com/css2?family=PT+Sans:wght@700&family=PT+Serif:wght@700&display=swap" rel="stylesheet">
<style>
  :root {
    --page: #ffffff;
    --frame-line: #111111;
    --paper-light: #f4ecd9;
    --paper-mid: #e9dcc0;
    --paper-edge: #d9c7a3;
    --headline-blue: #0b63c9;
    --headline-outline: #ffffff;
    --headline-shadow: rgba(40, 30, 10, 0.55);
    --write-ink: #4a4640;
    --pencil-light: #e8b45a;
    --pencil-dark: #c9a57a;
    --button-red: #d8161b;
    --button-red-dark: #8e0a0d;
    --button-text: #ffffff;
    --note-ink: #111111;
  }
  html, body {
    margin: 0;
    width: 1200px;
    height: 900px;
    overflow: hidden;
    background: var(--page);
  }
  .storyline {
    position: relative;
    width: 1200px;
    height: 900px;
  }
  .frame {
    position: absolute;
    left: 10px;
    width: 928px;
    height: 116px;
    border: 2px solid var(--frame-line);
    overflow: hidden;
    background: radial-gradient(ellipse at 55% 45%, var(--paper-light) 0%, var(--paper-mid) 60%, var(--paper-edge) 100%);
  }
  .headline {
    position: absolute;
    margin: 0;
    white-space: nowrap;
    font-family: "PT Sans", "Myriad Pro", sans-serif;
    font-weight: 700;
    color: var(--headline-blue);
    -webkit-text-stroke: 8px var(--headline-outline);
    paint-order: stroke fill;
    text-shadow: 4px 5px 6px var(--headline-shadow);
    line-height: 1;
    letter-spacing: -0.5px;
  }
  .headline-large { font-size: 84px; }
  .headline-small { font-size: 68px; }
  .hidden-lead { visibility: hidden; }
  .write-line {
    position: absolute;
    left: 44px;
    top: 30px;
    margin: 0;
    font-family: "PT Serif", Georgia, serif;
    font-weight: 700;
    font-size: 50px;
    color: var(--write-ink);
    line-height: 1;
    white-space: nowrap;
    letter-spacing: 1.5px;
  }
  .pencil-placeholder {
    position: absolute;
    width: 70px;
    height: 74px;
    border-radius: 4px;
    background: linear-gradient(135deg, var(--pencil-light) 0%, var(--pencil-dark) 100%);
    opacity: 0.55;
  }
  .click-button {
    position: absolute;
    left: 698px;
    top: 22px;
    width: 200px;
    height: 58px;
    border-radius: 8px;
    border: 2px solid var(--button-red-dark);
    background: linear-gradient(var(--button-red) 0%, var(--button-red) 55%, var(--button-red-dark) 100%);
    box-shadow: 3px 4px 6px rgba(0,0,0,0.5);
    color: var(--button-text);
    font-family: "PT Sans", Arial, sans-serif;
    font-weight: 700;
    font-size: 32px;
    letter-spacing: -0.5px;
    text-align: center;
    line-height: 56px;
    text-shadow: 1px 2px 2px rgba(0,0,0,0.6);
  }
  .note {
    position: absolute;
    left: 950px;
    width: 250px;
    margin: 0;
    text-align: center;
    font-family: Arial, Helvetica, sans-serif;
    font-size: 17px;
    line-height: 19px;
    color: var(--note-ink);
  }
  .note strong { font-weight: 700; }
</style>
</head>
<body>
<main class="storyline">

  <section class="frame" style="top:4px">
    <p class="headline headline-large" style="left:-4px; top:14px;">u can</p>
  </section>

  <section class="frame" style="top:132px">
    <p class="headline headline-large" style="left:28px; top:12px;">You can</p>
    <p class="headline headline-large" style="left:28px; top:104px;"><span class="hidden-lead">You can </span>'be the reporter'</p>
  </section>

  <section class="frame" style="top:260px">
    <p class="headline headline-large" style="left:26px; top:14px;">You can 'be the reporter'</p>
  </section>

  <section class="frame" style="top:388px">
    <p class="headline headline-small" style="left:104px; top:24px;">You can 'be the reporter'</p>
  </section>

  <section class="frame" style="top:516px">
    <p class="write-line">Write yo</p>
    <div class="pencil-placeholder" style="left:262px; top:0" role="img" aria-label="Pencil writing the text, with its shadow"></div>
  </section>

  <section class="frame" style="top:644px">
    <p class="write-line">Write your own</p>
    <div class="pencil-placeholder" style="left:420px; top:0" role="img" aria-label="Pencil writing the text, with its shadow"></div>
  </section>

  <section class="frame" style="top:772px">
    <p class="write-line">Write your own news</p>
    <div class="pencil-placeholder" style="left:608px; top:14px" role="img" aria-label="Pencil resting after writing, with its shadow"></div>
    <div class="click-button">Click Here</div>
  </section>

  <p class="note" style="top:8px">FLASH BANNER<br>FILE SIZE 10KB<br><strong>ANIMATION STORYLINE</strong></p>
  <p class="note" style="top:100px">TEXT FROM LEFT TO RIGHT</p>
  <p class="note" style="top:232px">TEXT FROM BOTTOM</p>
  <p class="note" style="top:364px">ZOOM OUT &nbsp;80%<br>, ZOOM IN 100%<br>3 TIMES</p>
  <p class="note" style="top:606px">PENCIL WRITE EFFECT<br>ANIMATION</p>
  <p class="note" style="top:774px">CLICK HERE BTN POP UP<br>3 TIMES<br>OR ON ROLL OVER</p>

</main>
</body>
</html>
```